Web Design Project: Facility Management company

Hi! We need a new website.

Our current website: http://www.vireo-trade.ru/ and we don-t like it. =)
The structure of our company has changed and now we don't need "cleaning" and "engeneering" on this site.

We are facility management company in Russia. So we provide integrated service solutions specific to industrial services: maintenance, repair, etc. of engineering systems.
More services:
Energy planning
Automation
Audit
Statements with regulators
Video surveillance
Central heating
Security systems
Welding
Management of subcontractors
Electrical installation and service needs
Reception
Catering

Visitors:
* Managers in the field of commercial real estate
* Chief engineers
* TOP managers of large companies, malls, factories...
+ their subordinates
* Small% of applicants.

Here you can see some websites/patterns we liked:
http://www.kobalmire.ru/ (This is our competitor’s site, so our site shouldn’t be an exact copy))))
http://www.dwatqo.ru/
http://www.layoutfarrow.com/demo/24296.html
http://www.layoutfarrow.com/website-templates/10145.html

Style:
Light, hi-tech/minimalizm, the color palette should be based on the original site colors (Green + black + white). http://www.vireo-trade.ru/

Estimated sitemap:
1. Home
2. About Us
3. Company's policy
4. History + Achievements.
5. Certificates
6. Map of presence (Here you can use sample map in file "our projects")
7. Services
8. Portfolio
9. News or blog
10. Jobs
11. Contacts - with the feedback form (or the function "call to order")
12. English

Need a design pages: main page, page 404. The rest of the page could be created by general pattern.

Logo, navigation bar and contacts should be visible on all pages of a site.
Flash animation elements and buttons, etc. - not needed.

* We need to develop 3 websites, so we are looking for a long term cooperation.
Looking forward to your creativity =)

Must Have:
Clear, intuitive structure of web pages.
In the center - of pictures reflecting our main services (industrial theme). May be in rotation.
BUT! This banner (central picture) should not be a huge one =)
All relevant information should be visible at once without scrolling.

A possibility to place media files (presentations, video ...) and 2 banner links on the main page.

Font should be available in Cyrillic.
Updates

IMPORTANT!

Please notice that in thisdesign we don't need "cleaning" and "engeneering" on this site.

So don't use old block of 4pictures from our current website. We don't need it anymore. 

Thestructure of our company has changed and now we need some links (may be banners,may be something else) to our future cleaning website as well as engeneeringwebsite.
It should look like seperate (partner) companies, not like our sevices.

Regards, Vera.

Please don't forget that we need bilingual site.

So define language changing tool in your designs.

Industry/Entity Type

Industrial

```html
<!DOCTYPE html>
<html lang="en">
<head>
<meta charset="utf-8">
<title>Vireo Trade — Facility Management</title>
<link href="https://fonts.googleapis.com/css2?family=Marmelad&display=swap" rel="stylesheet">
<style>
  :root {
    --green: #b6d432;
    --green-dark: #8fb51c;
    --green-text: #8ab51a;
    --ink: #111;
    --grey-bar: #f0f0f0;
    --nav-text: #555;
    --dark: #1e1e1e;
    --dark-2: #141414;
    --footer-text: #d8d8d8;
    --white: #fff;
  }
  * { box-sizing: border-box; margin: 0; padding: 0; }
  html, body { width: 1200px; height: 859px; overflow: hidden; background: var(--white); }
  body { position: relative; font-family: "Marmelad", sans-serif; color: var(--ink); }
  a { color: inherit; text-decoration: none; }
  .abs { position: absolute; white-space: nowrap; }

  .top-bar { left: 0; top: 0; width: 1200px; height: 22px; background: var(--grey-bar); }
  .top-links { right: 160px; top: 4px; display: flex; font-size: 12px; color: var(--nav-text); text-transform: uppercase; }
  .top-links span { padding: 0 23px; }
  .top-links .sep { padding: 0; }

  .logo { left: 170px; top: 44px; display: flex; align-items: center; gap: 10px; }
  .logo-mark { width: 34px; height: 34px; background: var(--green); border-radius: 50%; }
  .logo-name { font-size: 28px; letter-spacing: 2px; color: var(--ink); text-transform: uppercase; }

  .search { left: 502px; top: 48px; width: 295px; height: 23px; border: 1px solid #bbb; display: flex; align-items: center; background: var(--white); }
  .search-field { flex: 1; padding-left: 8px; font-size: 13px; color: #aaa; }
  .search-go { width: 34px; height: 17px; margin-right: 3px; background: #222; color: var(--white); font-size: 12px; text-align: center; line-height: 17px; }

  .lang { left: 882px; top: 51px; display: flex; align-items: center; font-size: 12px; color: var(--nav-text); text-transform: uppercase; }
  .flag { display: inline-block; width: 20px; height: 11px; margin-right: 6px; }
  .flag-en { background: #27408b; }
  .flag-ru { background: linear-gradient(#fff 0 33%, #2a4fc4 33% 66%, #d52b1e 66%); border: 1px solid #ccc; }
  .lang .sep { margin: 0 11px; }

  .main-nav { left: 161px; top: 117px; display: flex; font-size: 11px; color: var(--nav-text); text-transform: uppercase; }
  .main-nav span { padding: 0 8px; }
  .main-nav span:first-child { padding-left: 0; }

  .phone { left: 816px; top: 88px; font-size: 21px; line-height: 24px; color: var(--green-text); }
  .email { left: 817px; top: 112px; font-size: 16px; line-height: 20px; color: #444; }
  .contact-badge { left: 978px; top: 87px; }

  .hero { left: 0; top: 143px; width: 1200px; height: 327px; background: linear-gradient(90deg, #bcd93a, #b2d22c 60%, #aacb22); overflow: hidden; }
  .hero-photo { left: 600px; top: 0; width: 380px; height: 327px; background: linear-gradient(180deg, #c9d4c0 0%, #4a4d55 55%, #2c2f36 100%); border-radius: 140px 140px 0 0; opacity: .85; }
  .hero-title { left: 157px; top: 52px; font-size: 53px; line-height: 52px; color: #0c0c0c; text-transform: uppercase; }
  .hero-text { left: 157px; top: 182px; font-size: 27px; line-height: 34px; color: var(--white); }
  .hero-dots { left: 992px; top: 308px; display: flex; gap: 10px; }
  .hero-dots i { width: 9px; height: 9px; border-radius: 50%; background: var(--white); }
  .hero-dots i:first-child { background: #9fbd23; }

  .services { left: 0; top: 470px; width: 1200px; height: 362px; background: var(--dark); }
  .service-card { top: 47px; width: 206px; height: 140px; transform: skewX(-4deg); border-radius: 8px; border: 2px solid #000; overflow: hidden; }
  .card-title { position: absolute; font-size: 28px; line-height: 28px; text-transform: uppercase; transform: skewX(4deg); white-space: nowrap; }
  .card-energy { left: 186px; background: linear-gradient(135deg, #5fe3c0, #2fbfa0); }
  .card-video { left: 397px; background: linear-gradient(135deg, #f07a45, #d9481c); }
  .card-security { left: 607px; background: linear-gradient(135deg, #f7c52e, #eea51a); }
  .card-heating { left: 817px; background: linear-gradient(135deg, #8fd0f7, #4fa6e3); }
  .view-btn { top: 173px; width: 147px; height: 38px; border-radius: 5px; background: linear-gradient(#4a4a4a, #151515); border: 1px solid #000; color: var(--white); font-size: 13px; text-transform: uppercase; display: flex; align-items: center; justify-content: space-between; padding: 0 14px 0 16px; transform: skewX(-4deg); }
  .view-btn svg { transform: skewX(4deg); flex: none; }
  .slide-arrow { top: 105px; }

  .divider { left: 130px; top: 236px; width: 940px; height: 1px; background: linear-gradient(90deg, transparent, #3a3a3a 20%, #3a3a3a 80%, transparent); }

  .social-row { left: 162px; display: flex; align-items: center; gap: 14px; }
  .social-icon { width: 22px; height: 22px; background: #5b8bd0; border-radius: 3px; }
  .social-count { width: 85px; height: 28px; background: #050505; border: 1px solid #333; border-radius: 3px; color: var(--footer-text); font-size: 11px; line-height: 26px; padding-left: 14px; }
  .footer-col { top: 265px; font-family: Arial, Helvetica, sans-serif; font-size: 11.5px; line-height: 17px; color: var(--footer-text); }
  .footer-col strong { color: var(--green); }
  .connect-title { left: 943px; top: 264px; font-size: 12px; color: var(--green); text-transform: uppercase; }
  .connect-item { left: 943px; display: flex; align-items: center; gap: 13px; font-size: 12px; color: var(--footer-text); text-transform: uppercase; }
  .connect-square { width: 21px; height: 21px; background: #3a3a3a; border-radius: 3px; }

  .copyright { left: 0; top: 832px; width: 1200px; height: 27px; background: var(--dark-2); border-top: 1px solid #3a3a3a; text-align: center; font-family: Arial, Helvetica, sans-serif; font-size: 10.5px; line-height: 26px; color: var(--footer-text); }
</style>
</head>
<body>
  <div class="abs top-bar"></div>
  <nav class="abs top-links">
    <span>Portfolio</span><span class="sep">|</span><span>News or blog</span><span class="sep">|</span><span>Jobs</span><span class="sep">|</span><span>Sevice</span>
  </nav>

  <div class="abs logo">
    <span class="logo-mark"></span>
    <span class="logo-name">Vireo Trade</span>
  </div>

  <div class="abs search">
    <span class="search-field">SEARCH..</span>
    <span class="search-go">GO</span>
  </div>

  <div class="abs lang">
    <span class="flag flag-en"></span>English<span class="sep">|</span><span class="flag flag-ru"></span>Russia
  </div>

  <nav class="abs main-nav">
    <span>Home</span>|<span>About us</span>|<span>Company's policy</span>|<span>History &amp; achievements.</span>|<span>Certificates</span>|<span>Map of presence</span>
  </nav>

  <div class="abs phone">+7812 400 3186</div>
  <div class="abs email">info@vireotrade.com</div>
  <svg class="abs contact-badge" width="64" height="64" viewBox="0 0 64 64" aria-hidden="true">
    <defs><linearGradient id="badge" x1="0" y1="0" x2="0" y2="1"><stop offset="0" stop-color="#5a5a5a"/><stop offset="1" stop-color="#111"/></linearGradient></defs>
    <path d="M6 2h56a2 2 0 0 1 2 2v50H40l-8 9-8-9H6a4 4 0 0 1-4-4V6a4 4 0 0 1 4-4z" fill="url(#badge)"/>
    <path d="M22 14c2-3 18-3 20 0l-2 5h-4l-1-2h-6l-1 2h-4z" fill="#b6d432"/>
    <rect x="20" y="26" width="26" height="17" rx="2" fill="#fff"/>
    <path d="M20 27l13 9 13-9" fill="none" stroke="#222" stroke-width="2"/>
  </svg>

  <section class="abs hero">
    <div class="abs hero-photo" role="img" aria-label="Photo of an engineer in a suit holding a hard hat and rolled drawings"></div>
    <h1 class="abs hero-title">Delenit augue<br>feugait nulla</h1>
    <p class="abs hero-text">Ut wisi enim ad minim<br>veniam, quis nostrud exerci<br>molestie consequat, vel illum</p>
    <div class="abs hero-dots"><i></i><i></i><i></i></div>
  </section>

  <section class="abs services">
    <svg class="abs slide-arrow" style="left:161px" width="20" height="24" viewBox="0 0 20 24" aria-hidden="true"><path d="M16 2L4 12l12 10" fill="none" stroke="#b6d432" stroke-width="5"/></svg>

    <div class="abs service-card card-energy" role="img" aria-label="Energy planning illustration with a light bulb">
      <span class="card-title" style="left:18px;top:40px;color:#f5e22a">Energi</span>
      <span class="card-title" style="left:34px;top:70px;color:#fff;font-size:24px">Planning</span>
    </div>
    <div class="abs view-btn" style="left:188px">View website
      <svg width="16" height="16" viewBox="0 0 16 16"><circle cx="8" cy="8" r="7" fill="none" stroke="#45d2b2" stroke-width="2"/><path d="M6 4l4 4-4 4" fill="none" stroke="#45d2b2" stroke-width="2"/></svg></div>

    <div class="abs service-card card-video" role="img" aria-label="Video surveillance illustration with a running figure">
      <span class="card-title" style="left:74px;top:10px;color:#fff">Video</span>
      <span class="card-title" style="left:56px;top:64px;color:#fff;font-size:17px">Surveillance</span>
    </div>
    <div class="abs view-btn" style="left:399px">View website
      <svg width="16" height="16" viewBox="0 0 16 16"><circle cx="8" cy="8" r="7" fill="none" stroke="#e2582a" stroke-width="2"/><path d="M6 4l4 4-4 4" fill="none" stroke="#e2582a" stroke-width="2"/></svg></div>

    <div class="abs service-card card-security" role="img" aria-label="Security systems illustration with a shield and tick">
      <span class="card-title" style="left:14px;top:58px;color:#222;font-size:19px">Security</span>
      <span class="card-title" style="left:18px;top:82px;color:#fff;font-size:17px">Systems</span>
      <svg class="abs" style="left:118px;top:22px" width="70" height="84" viewBox="0 0 70 84"><path d="M35 2l32 10v28c0 22-16 36-32 42C19 76 3 62 3 40V12z" fill="#777"/><path d="M35 9l26 8v23c0 18-13 30-26 35C22 70 9 58 9 40V17z" fill="#6fb62a"/><path d="M20 42l11 11 20-24" fill="none" stroke="#fff" stroke-width="7"/></svg>
    </div>
    <div class="abs view-btn" style="left:609px">View website
      <svg width="16" height="16" viewBox="0 0 16 16"><circle cx="8" cy="8" r="7" fill="none" stroke="#f0b020" stroke-width="2"/><path d="M6 4l4 4-4 4" fill="none" stroke="#f0b020" stroke-width="2"/></svg></div>

    <div class="abs service-card card-heating" role="img" aria-label="Central heating illustration with a house in a knitted hat">
      <span class="card-title" style="left:84px;top:28px;color:#fff;font-size:22px">Central</span>
      <span class="card-title" style="left:90px;top:52px;color:#e0332a;font-size:22px">Heating</span>
    </div>
    <div class="abs view-btn" style="left:819px">View website
      <svg width="16" height="16" viewBox="0 0 16 16"><circle cx="8" cy="8" r="7" fill="none" stroke="#4aa3e0" stroke-width="2"/><path d="M6 4l4 4-4 4" fill="none" stroke="#4aa3e0" stroke-width="2"/></svg></div>

    <svg class="abs slide-arrow" style="left:1022px" width="20" height="24" viewBox="0 0 20 24" aria-hidden="true"><path d="M4 2l12 10L4 22" fill="none" stroke="#b6d432" stroke-width="5"/></svg>

    <div class="abs divider"></div>

    <div class="abs social-row" style="top:267px"><span class="social-icon"></span><span class="social-count">1,555 Likes</span></div>
    <div class="abs social-row" style="top:306px"><span class="social-icon" style="background:#2aa3e0"></span><span class="social-count">155 Posts</span></div>

    <div class="abs footer-col" style="left:363px">
      <strong>Vireo Trade</strong><br>190000, St. Petersburg<br>ul. Lesnaya Alleya, 14<br>Mailing address: 196700<br>St. Petersburg, Ozernaya, 7
    </div>
    <div class="abs footer-col" style="left:586px">Home<br>About Us<br>Company's policy<br>History &amp; Achievements.<br>Certificates</div>
    <div class="abs footer-col" style="left:784px">Map of presence<br>Services<br>Portfolio<br>News or blog<br>Jobs</div>

    <div class="abs connect-title">Connect with us</div>
    <div class="abs connect-item" style="top:291px"><span class="connect-square"></span>Friendwall</div>
    <div class="abs connect-item" style="top:321px"><span class="connect-square"></span>Chirpline</div>
  </section>

  <footer class="abs copyright">© Copyright 2012 Vireo Trade &nbsp;All rights reserved.</footer>
</body>
</html>
```